Heron Trade finance web design

We are a newly established business which provides invoice finance to Small Businesses in England and Wales.
Our approach is very much a funder where the small business owner can talk to the decision maker. We will guarantee on receipt of information, a decision within 24 hours.
We are not a bank so the look of the website need to be friendly but professional.
Have two types of people we are trying to attract to the website: 1) partners who are small business owners and 2) introducers who is accountants and commercial brokers who introduce us to the small businesses.
Currently no website, although domain has been reserved.
The design should be:
Professional
“Clean” Look
Designed to convey Trust and Authority.
Appeal to the small business owner.
Must incorporate:
Logo (attached)
Front page:Top tabs to other pages 1) About us 2) Services 3) Introducers 4) Contact us
Need picture and logo on page.
1) About us page- Room for talk about the company, the people and our critera.
2) Services page- We need for what invoice finance is, and 5 boxes for different services we will provide. (link on page to contact us)
3) Introducers page- We need a part for why become an introducer? Who we can help? Why we are different? (link on page to contact us)
4) Contact us page- Office address, email, tel and if possible a map and a contact me part which will email direct to us.
Text will be provided for the design, if we can see the setup of the website we will provide a part for each of the pages to support.
Styles we think convey the correct image:
www.brindlecapital.example
www.tollmarkfs.example
www.qelfunding.example
Small business owners
Finance
5+ page

```html
<!DOCTYPE html>
<html lang="en">
<head>
<meta charset="utf-8">
<title>Heron Trade finance</title>
<link rel="stylesheet" href="https://fonts.googleapis.com/css2?family=Open+Sans:wght@300;400;600;700&display=swap">
<style>
  :root {
    --brand-red: #b80c1c;
    --heading-red: #b3141f;
    --ink: #222222;
    --body-grey: #6a6a6a;
    --light-panel: #e9e9e9;
    --footer-bg: #1f1f1f;
    --footer-text: #a9a9a9;
    --white: #ffffff;
  }
  * { box-sizing: border-box; margin: 0; padding: 0; }
  html, body { width: 824px; height: 1200px; overflow: hidden; }
  body { font-family: "Open Sans", Arial, sans-serif; background: var(--white); color: var(--body-grey); position: relative; }

  .site-header { position: absolute; top: 0; left: 0; width: 824px; height: 75px; border-bottom: 1px solid #eee; background: var(--white); }
  .brand { position: absolute; left: 90px; top: 26px; font-size: 20px; font-weight: 700; color: var(--brand-red); letter-spacing: -0.3px; }
  .account-actions { position: absolute; right: 92px; top: 15px; display: flex; gap: 4px; }
  .account-actions a { display: block; height: 22px; line-height: 22px; padding: 0 11px; font-size: 7.5px; color: var(--white); text-decoration: none; letter-spacing: 0.2px; }
  .btn-login { background: #111; }
  .btn-register { background: var(--brand-red); }
  .main-nav { position: absolute; right: 92px; top: 51px; display: flex; gap: 19px; }
  .main-nav a { font-size: 8px; color: #333; text-decoration: none; letter-spacing: 0.2px; }
  .main-nav a.is-active { color: var(--brand-red); }

  .hero { position: absolute; top: 75px; left: 0; width: 824px; height: 347px;
    background: linear-gradient(120deg, #dfe9f2 0%, #c7d7e6 40%, #6f7c89 70%, #1f262e 100%); }
  .slider-arrow { position: absolute; top: 163px; width: 17px; height: 21px; }
  .slider-arrow.prev { left: 0; background: rgba(200,200,200,0.85); }
  .slider-arrow.next { right: 0; }

  .feature-band { position: absolute; top: 422px; left: 0; width: 824px; height: 186px; background: var(--brand-red); color: var(--white); }
  .feature { position: absolute; top: 28px; width: 200px; text-align: center; }
  .feature svg { display: block; margin: 0 auto; }
  .feature h3 { font-size: 13.5px; font-weight: 400; margin-top: 18px; letter-spacing: 0.2px; }
  .feature p { font-size: 7.2px; line-height: 12px; margin-top: 5px; color: #f3c6ca; }
  .feature .btn-outline { display: inline-block; margin-top: 10px; border: 1px solid #f1b5ba; padding: 5px 9px; font-size: 7.2px; color: var(--white); text-decoration: none; }

  .intro-panel { position: absolute; top: 608px; left: 0; width: 824px; height: 236px; background: radial-gradient(ellipse at 70% 50%, #f7f7f7 0%, var(--light-panel) 70%); }
  .section-title { font-size: 16.5px; font-weight: 400; color: var(--heading-red); letter-spacing: 0.1px; }
  .section-copy { font-size: 7.4px; line-height: 13.2px; color: var(--body-grey); margin-top: 10px; }
  .intro-text { position: absolute; left: 91px; top: 33px; width: 280px; }
  .btn-plain { display: inline-block; margin-top: 12px; padding: 6px 9px; font-size: 7.2px; color: #555; text-decoration: none; }
  .intro-text .btn-plain { background: var(--white); }
  .invoice-art { position: absolute; left: 398px; top: 32px; width: 334px; height: 184px; border-radius: 6px;
    background: linear-gradient(180deg, #d9d9d9 0%, #cfcfcf 60%, #e2e2e2 100%); }

  .growth-panel { position: absolute; top: 844px; left: 0; width: 824px; height: 246px; background: var(--white); }
  .growth-art { position: absolute; left: 90px; top: 42px; width: 164px; height: 164px;
    background: linear-gradient(180deg, #f6dc5a 0%, #8fd8c0 55%, #2fae8c 100%); border-radius: 4px; }
  .growth-text { position: absolute; left: 287px; top: 40px; width: 445px; }
  .growth-text .btn-plain { background: #ededed; margin-top: 15px; }

  .site-footer { position: absolute; top: 1090px; left: 0; width: 824px; height: 110px; background: var(--footer-bg); color: var(--footer-text); }
  .contact-row { position: absolute; left: 90px; top: 18px; width: 642px; height: 28px; border-bottom: 1px solid #3a3a3a; font-size: 7.8px; }
  .contact-item { position: absolute; top: 0; display: flex; align-items: center; gap: 6px; }
  .social-links { position: absolute; right: 4px; top: 1px; display: flex; gap: 10px; }
  .social-links span { width: 7px; height: 7px; border-radius: 50%; background: #8a8a8a; display: block; }
  .footer-links { position: absolute; top: 62px; width: 824px; text-align: center; font-size: 6.6px; }
  .footer-links a { color: var(--footer-text); text-decoration: none; margin: 0 3px; }
  .copyright { position: absolute; top: 79px; width: 824px; text-align: center; font-size: 6.6px; }
</style>
</head>
<body>

<header class="site-header">
  <div class="brand">Heron Trade finance</div>
  <div class="account-actions">
    <a class="btn-login" href="#">LOGIN</a>
    <a class="btn-register" href="#">REGISTER</a>
  </div>
  <nav class="main-nav">
    <a class="is-active" href="#">HOME</a>
    <a href="#">ABOUT US</a>
    <a href="#">SERVICES</a>
    <a href="#">INTRODUCERS</a>
    <a href="#">CONTACT US</a>
  </nav>
</header>

<section class="hero" role="img" aria-label="Photograph of a businessman's hand pointing a pencil at financial charts on a clipboard">
  <div class="slider-arrow prev">
    <svg width="17" height="21" viewBox="0 0 17 21"><path d="M10 5 L6 10.5 L10 16" fill="none" stroke="#fff" stroke-width="1.2"/></svg>
  </div>
  <div class="slider-arrow next">
    <svg width="17" height="21" viewBox="0 0 17 21"><path d="M7 5 L11 10.5 L7 16" fill="none" stroke="#ccc" stroke-width="1.2"/></svg>
  </div>
</section>

<section class="feature-band">
  <div class="feature" style="left:90px">
    <svg width="26" height="30" viewBox="0 0 26 30" fill="none" stroke="#fff" stroke-width="1.8">
      <path d="M2 2 H17 L24 9 V28 H2 Z"/><path d="M17 2 V9 H24"/>
      <path d="M7 14 H19 M7 18 H19 M7 22 H19"/>
    </svg>
    <h3>INVOICE FINANCE</h3>
    <p>Proin molestie, ante vitae iaculis accumsan, dolor odio porttitor quam, in varius lectus tellus vitae metus. Aenean hendrerit erat sem, sit amet imperdiet</p>
    <a class="btn-outline" href="#">Read More</a>
  </div>
  <div class="feature" style="left:312px">
    <svg width="34" height="28" viewBox="0 0 34 28" fill="#fff">
      <rect x="1" y="1" width="2" height="26"/><rect x="1" y="25" width="32" height="2"/>
      <rect x="8" y="14" width="3.5" height="9"/><rect x="14" y="8" width="3.5" height="15"/>
      <rect x="20" y="12" width="3.5" height="11"/><rect x="26" y="5" width="3.5" height="18"/>
    </svg>
    <h3>DONEC IMPERDIET</h3>
    <p>Proin molestie, ante vitae iaculis accumsan, dolor odio porttitor quam, in varius lectus tellus vitae metus. Aenean hendrerit erat sem, sit amet imperdiet</p>
    <a class="btn-outline" href="#">Read More</a>
  </div>
  <div class="feature" style="left:534px">
    <svg width="26" height="30" viewBox="0 0 26 30">
      <rect x="1.5" y="1.5" width="23" height="27" rx="2" fill="none" stroke="#fff" stroke-width="1.8"/>
      <rect x="5" y="5" width="16" height="5" fill="#fff"/>
      <g fill="#fff">
        <circle cx="7" cy="14" r="1.6"/><circle cx="11" cy="14" r="1.6"/><circle cx="15" cy="14" r="1.6"/><circle cx="19" cy="14" r="1.6"/>
        <circle cx="7" cy="19" r="1.6"/><circle cx="11" cy="19" r="1.6"/><circle cx="15" cy="19" r="1.6"/><circle cx="19" cy="19" r="1.6"/>
        <circle cx="7" cy="24" r="1.6"/><circle cx="11" cy="24" r="1.6"/><circle cx="15" cy="24" r="1.6"/><circle cx="19" cy="24" r="1.6"/>
      </g>
    </svg>
    <h3>CRAS IPSUM METUS</h3>
    <p>Proin molestie, ante vitae iaculis accumsan, dolor odio porttitor quam, in varius lectus tellus vitae metus. Aenean hendrerit erat sem, sit amet imperdiet</p>
    <a class="btn-outline" href="#">Read More</a>
  </div>
</section>

<section class="intro-panel">
  <div class="intro-text">
    <h2 class="section-title">Donec imperdiet in leo id blandit</h2>
    <p class="section-copy">Nulla tristique rhoncus dui vitae auctor. Vivamus dictum fringilla magna, id molestie nulla consectetur vel. Sed quis blandit elit. Fusce eleifend pretium massa sed feugiat. Phasellus ut turpis sit amet tortor tincidunt efficitur. Phasellus ut pretium nulla. Proin molestie, ante vitae iaculis accumsan, dolor odio porttitor quam, in varius lectus tellus vitae metus. Aenean hendrerit erat sem, sit amet imperdiet velit pretium ut. Donec pretium dolor eu enim tempor fringilla. Aenean convallis mi id vestibulum malesuada. Vivamus eget dui in eros faucibus faucibus.</p>
    <a class="btn-plain" href="#">Read more</a>
  </div>
  <div class="invoice-art" role="img" aria-label="Illustration of a computer monitor showing an invoice with a pay button, surrounded by coins, a calculator, bank cards and banknotes"></div>
</section>

<section class="growth-panel">
  <div class="growth-art" role="img" aria-label="Illustration of a stack of green banknotes with a yellow rising arrow above"></div>
  <div class="growth-text">
    <h2 class="section-title">Etiam ut elit sit amet felis eleifend molestie</h2>
    <p class="section-copy">Nulla tristique rhoncus dui vitae auctor. Vivamus dictum fringilla magna, id molestie nulla consectetur vel. Sed quis blandit elit. Fusce eleifend pretium massa sed feugiat. Phasellus ut turpis sit amet tortor tincidunt efficitur. Phasellus ut pretium nulla. Proin molestie, ante vitae iaculis accumsan, dolor odio porttitor quam, in varius lectus tellus vitae metus. Aenean hendrerit erat sem, sit amet imperdiet velit pretium ut. Donec pretium dolor eu enim tempor fringilla. Aenean convallis mi id vestibulum malesuada. Vivamus eget dui in eros faucibus faucibus. Pellentesque habitant morbi tristique senectus et netus et malesuada fames ac turpis egestas. Vestibulum ultricies sem nec congue blandit. Pellentesque imperdiet, urna sit amet finibus posuere, lectus mauris sollicitudin ligula</p>
    <a class="btn-plain" href="#">Read more</a>
  </div>
</section>

<footer class="site-footer">
  <div class="contact-row">
    <div class="contact-item" style="left:0">
      <svg width="7" height="10" viewBox="0 0 7 10"><path d="M3.5 0 C1.5 0 0 1.5 0 3.4 C0 6 3.5 10 3.5 10 C3.5 10 7 6 7 3.4 C7 1.5 5.5 0 3.5 0 Z" fill="#a9a9a9"/><circle cx="3.5" cy="3.5" r="1.3" fill="#1f1f1f"/></svg>
      <span>24 Building name, Street name, City - Zipcode</span>
    </div>
    <div class="contact-item" style="left:228px">
      <svg width="9" height="9" viewBox="0 0 9 9"><path d="M1.5 0.5 L3 0.5 L3.8 2.6 L2.8 3.4 C3.3 4.6 4.4 5.7 5.6 6.2 L6.4 5.2 L8.5 6 L8.5 7.5 C8.5 8.1 8 8.5 7.4 8.5 C3.6 8.3 0.7 5.4 0.5 1.6 C0.5 1 0.9 0.5 1.5 0.5 Z" fill="#a9a9a9"/></svg>
      <span>Call Now : 555 014 2290</span>
    </div>
    <div class="contact-item" style="left:380px">
      <svg width="11" height="8" viewBox="0 0 11 8"><rect x="0" y="0" width="11" height="8" fill="#a9a9a9"/><path d="M0 0 L5.5 4.5 L11 0" fill="none" stroke="#1f1f1f" stroke-width="1"/></svg>
      <span>Email:&nbsp; info@herontradefinance.example</span>
    </div>
    <div class="social-links" aria-label="Social links"><span></span><span></span><span></span></div>
  </div>
  <nav class="footer-links">
    <a href="#">Home</a>|<a href="#">About us</a>|<a href="#">Services</a>|<a href="#">Introducers</a>|<a href="#">Contact us</a>
  </nav>
  <p class="copyright">Copyright &copy; 2016 Heron Trade finance.&nbsp;&nbsp; All rights reserved.</p>
</footer>

</body>
</html>
```